Forensic Document Examiner, looking for contemporary update to my stationery design.

Looking for professional, classy logo design for stationery and business cards. My current stationery and business card is attached.I believe a logo image makes a header section interesting, so an intriguing design of a pen, feathered pen, microscope, magnifying glass, etc., would be appropriate. I have been in the business for over 30 years. I leave ideas to the imagination of the designer.My work involves mainly, the comparison of signatures and handwriting. I also resolve alterations, obliterations, and work as shown on my website: www.documentexaminer.infoThe image produced will be printed on quality white stationery and envelopes. The stationery will be photocopied by my clients, so the images should be reproducible. The business cards may be designed in other than white.

Target Market(s)

Attorneys

Font styles to use
Sans Serif

Colors

Designer to choose colors to be used in the design.

Requirements
Must have
• Image suitable for white stationery and photocopying.
• Classy logo and image; no casual fonts.
Nice to have
• Intriguing, contemporary design incorporating a relevant logo to my work.

```html
<!DOCTYPE html>
<html lang="en">
<head>
<meta charset="utf-8">
<title>Quill Verity Stationery</title>
<link href="https://fonts.googleapis.com/css2?family=Cinzel:wght@400;500&family=Crimson+Text&display=swap" rel="stylesheet">
<style>
  :root {
    --backdrop: #383838;
    --brand-blue: #1272ba;
    --paper: #ffffff;
    --ink: #111111;
    --rule: #7a7a7a;
    --label: #e6e6e6;
  }
  * { margin: 0; padding: 0; box-sizing: border-box; }
  html, body { width: 787px; height: 1200px; overflow: hidden; background: var(--backdrop); }
  .sheet { position: relative; width: 787px; height: 1200px; font-family: "Cinzel", serif; }
  .view-label { position: absolute; top: 45px; font-size: 11px; color: var(--label); letter-spacing: .5px; transform: translateX(-50%); }
  .card { position: absolute; top: 72px; width: 276px; height: 154px; overflow: hidden; }
  .card-front { left: 76px; background: var(--brand-blue); border-top-left-radius: 24px; color: var(--paper); }
  .card-back { left: 438px; background: var(--paper); border-top-right-radius: 24px; color: var(--ink); }
  .abs { position: absolute; }
  .wordmark { position: absolute; display: flex; flex-direction: column; align-items: center; text-align: center; font-family: "Cinzel", serif; font-weight: 500; line-height: 1.15; }
  .wordmark .dot { border-radius: 50%; margin-bottom: 5px; }
  .front-wordmark { left: 95px; top: 45px; width: 90px; font-size: 13px; color: var(--paper); }
  .front-wordmark .dot { width: 12px; height: 12px; background: var(--paper); }
  .front-title { left: 193px; top: 17px; font-size: 12px; line-height: 19.5px; }
  .back-wordmark { left: 4px; top: 30px; width: 56px; font-size: 8px; color: var(--brand-blue); }
  .back-wordmark .dot { width: 8px; height: 8px; background: var(--brand-blue); }
  .back-band { position: absolute; left: 0; top: 0; }
  .back-name { left: 68px; top: 20px; font-size: 14px; white-space: nowrap; }
  .back-role { left: 68px; top: 37px; font-size: 7px; white-space: nowrap; }
  .back-contact { font-size: 6.5px; white-space: nowrap; }
  .back-contact.email { font-family: "Crimson Text", serif; font-size: 6.5px; }
  .rule-v { position: absolute; width: 1px; background: var(--rule); }
  .icon { position: absolute; }
  .letterhead { position: absolute; left: 65px; top: 286px; width: 659px; height: 859px; background: var(--paper); color: var(--ink); }
  .lh-wordmark { left: 6px; top: 66px; width: 90px; font-size: 12px; color: var(--ink); }
  .lh-wordmark .dot { width: 12px; height: 12px; background: var(--ink); }
  .lh-name { left: 110px; top: 47px; font-size: 20px; white-space: nowrap; }
  .lh-role { left: 110px; top: 70px; font-size: 11px; white-space: nowrap; }
  .lh-address { left: 110px; top: 110px; font-size: 11px; line-height: 13.5px; }
  .lh-contact { left: 470px; font-family: "Crimson Text", serif; font-size: 12px; white-space: nowrap; }
</style>
</head>
<body>
<main class="sheet">
  <span class="view-label" style="left:215px">Front</span>
  <span class="view-label" style="left:570px">Back</span>

  <section class="card card-front">
    <div class="wordmark front-wordmark"><span class="dot"></span>Quill<br>Verity</div>
    <p class="abs front-title">Forensic<br>Document<br>Examiner</p>
  </section>

  <section class="card card-back">
    <svg class="back-band" width="276" height="154" aria-hidden="true">
      <polygon points="0,120 61,120 78,132 276,132 276,154 0,154" fill="var(--brand-blue)"/>
    </svg>
    <div class="wordmark back-wordmark"><span class="dot"></span>Quill<br>Verity</div>
    <span class="rule-v" style="left:61px;top:10px;height:110px"></span>
    <h1 class="abs back-name" style="font-weight:400">Daniel R. Whitlock</h1>
    <p class="abs back-role">Forensic Document Examiner</p>
    <span class="rule-v" style="left:164px;top:75px;height:53px"></span>
    <svg class="icon" style="left:153px;top:80px" width="8" height="11" viewBox="0 0 8 11" aria-hidden="true">
      <path d="M4 0a4 4 0 0 1 4 4c0 3-4 7-4 7S0 7 0 4a4 4 0 0 1 4-4z" fill="var(--brand-blue)"/><circle cx="4" cy="4" r="1.5" fill="#fff"/>
    </svg>
    <p class="abs back-contact" style="left:168px;top:79px;line-height:9.5px">P. O. Box 2184<br>Salem Or 97301</p>
    <svg class="icon" style="left:153px;top:101px" width="9" height="10" viewBox="0 0 24 24" aria-hidden="true">
      <path d="M6.6 10.8a15 15 0 0 0 6.6 6.6l2.2-2.2c.3-.3.7-.4 1-.2 1.1.4 2.3.6 3.6.6.6 0 1 .4 1 1V20c0 .6-.4 1-1 1A17 17 0 0 1 3 4c0-.6.4-1 1-1h3.5c.6 0 1 .4 1 1 0 1.3.2 2.5.6 3.6.1.3 0 .7-.2 1z" fill="var(--brand-blue)"/>
    </svg>
    <p class="abs back-contact" style="left:168px;top:102px">(555) 310-2746</p>
    <svg class="icon" style="left:150px;top:117px" width="14" height="10" viewBox="0 0 14 10" aria-hidden="true">
      <rect x=".5" y=".5" width="13" height="9" fill="none" stroke="var(--brand-blue)"/><path d="M.5 .5 7 6l6.5-5.5M.5 9.5 5 5M13.5 9.5 9 5" fill="none" stroke="var(--brand-blue)"/>
    </svg>
    <p class="abs back-contact email" style="left:168px;top:116px">dwhitlock@quillverity.example</p>
  </section>

  <section class="letterhead">
    <div class="wordmark lh-wordmark"><span class="dot"></span>Quill<br>Verity</div>
    <span class="rule-v" style="left:101px;top:35px;height:104px"></span>
    <h1 class="abs lh-name" style="font-weight:400">Daniel R. Whitlock</h1>
    <p class="abs lh-role">Forensic Document Examiner</p>
    <p class="abs lh-address">P. O. Box 2184<br>Salem Or 97301</p>
    <span class="rule-v" style="left:465px;top:35px;height:44px"></span>
    <svg class="icon" style="left:445px;top:39px" width="14" height="16" viewBox="0 0 24 24" aria-hidden="true">
      <path d="M6.6 10.8a15 15 0 0 0 6.6 6.6l2.2-2.2c.3-.3.7-.4 1-.2 1.1.4 2.3.6 3.6.6.6 0 1 .4 1 1V20c0 .6-.4 1-1 1A17 17 0 0 1 3 4c0-.6.4-1 1-1h3.5c.6 0 1 .4 1 1 0 1.3.2 2.5.6 3.6.1.3 0 .7-.2 1z" fill="var(--ink)"/>
    </svg>
    <p class="abs lh-contact" style="top:41px">(555) 310-2746</p>
    <svg class="icon" style="left:436px;top:63px" width="21" height="14" viewBox="0 0 21 14" aria-hidden="true">
      <rect x=".75" y=".75" width="19.5" height="12.5" fill="none" stroke="var(--ink)" stroke-width="1.5"/><path d="M.75 .75 10.5 8l9.75-7.25M.75 13.25 8 6.5M20.25 13.25 13 6.5" fill="none" stroke="var(--ink)" stroke-width="1.5"/>
    </svg>
    <p class="abs lh-contact" style="top:61px">dwhitlock@quillverity.example</p>
  </section>
</main>
</body>
</html>
```